Business card design needed

I need a business card design for a dog walking, dog minding and dog training business. Please refer to my website for the basic company colours and fonts I'm after. Planning on a double sided card, so all information doesn't need to be on the 'front' side.
Cheers

Industry/Entity Type

Dog Training

Contact Information for Business Card

Meadow Paws - happy hounds
Rua 0498307164
meadowpawsdemo.com.au
-walking
-holiday stays
-onsite care
-training and behavioural consultations

```html
<!DOCTYPE html>
<html lang="en">
<head>
<meta charset="utf-8">
<title>Meadow Paws – business card</title>
<link rel="stylesheet" href="https://fonts.googleapis.com/css2?family=Open+Sans:wght@300;400;600&display=swap">
<style>
  :root {
    --paper: #f1f8d0;
    --flame: #f53a00;
    --coral: #f26a4a;
    --slate: #3a4048;
    --sage-text: #b3bca4;
    --service-text: #6b7266;
    --swoosh: #d2dabb;
  }
  * { margin: 0; padding: 0; box-sizing: border-box; }
  html, body { width: 1200px; height: 693px; overflow: hidden; background: var(--paper); }
  .card {
    position: relative;
    width: 1200px;
    height: 693px;
    background: var(--paper);
    font-family: "Open Sans", sans-serif;
  }
  .brand { position: absolute; left: 65px; top: 66px; }
  .brand-name {
    font-size: 46px;
    font-weight: 600;
    letter-spacing: 1px;
    color: var(--flame);
    line-height: 1;
    text-transform: uppercase;
  }
  .brand-tagline {
    margin-top: 4px;
    font-size: 22px;
    font-weight: 300;
    color: var(--sage-text);
    line-height: 1.1;
  }
  .hero-dog {
    position: absolute;
    left: 65px;
    top: 178px;
    width: 680px;
    height: 408px;
    border-radius: 50%;
    background: radial-gradient(ellipse closest-side at 50% 50%, var(--flame) 0%, rgba(245,58,0,0.85) 55%, rgba(245,58,0,0.4) 85%, rgba(245,58,0,0) 100%);
  }
  .services {
    position: absolute;
    left: 820px;
    top: 214px;
    list-style: none;
  }
  .services li {
    display: flex;
    align-items: center;
    height: 32.5px;
    font-size: 21px;
    font-weight: 400;
    color: var(--service-text);
  }
  .paw { width: 22px; height: 22px; margin-right: 8px; flex: none; }
  .paw circle, .paw ellipse { fill: var(--coral); }
  .swoosh { position: absolute; left: 810px; top: 436px; width: 290px; height: 160px; }
  .contact {
    position: absolute;
    left: 861px;
    top: 479px;
    line-height: 25px;
    font-size: 24px;
    font-weight: 300;
    font-style: normal;
  }
  .contact-name { color: var(--flame); }
  .contact-phone { color: var(--coral); }
  .contact-web { color: var(--slate); font-weight: 400; }
</style>
</head>
<body>
<div class="card">
  <header class="brand">
    <div class="brand-name">Meadow Paws</div>
    <div class="brand-tagline">happy hounds</div>
  </header>

  <div class="hero-dog" role="img" aria-label="Orange silhouette of a running dog"></div>

  <ul class="services">
    <li><svg class="paw" viewBox="0 0 22 22"><ellipse cx="11" cy="14.5" rx="6" ry="5.5"/><circle cx="4" cy="8" r="2.4"/><circle cx="9" cy="4.5" r="2.4"/><circle cx="15" cy="5" r="2.4"/><circle cx="19" cy="9.5" r="2.2"/></svg>walking</li>
    <li><svg class="paw" viewBox="0 0 22 22"><ellipse cx="11" cy="14.5" rx="6" ry="5.5"/><circle cx="4" cy="8" r="2.4"/><circle cx="9" cy="4.5" r="2.4"/><circle cx="15" cy="5" r="2.4"/><circle cx="19" cy="9.5" r="2.2"/></svg>holiday stays</li>
    <li><svg class="paw" viewBox="0 0 22 22"><ellipse cx="11" cy="14.5" rx="6" ry="5.5"/><circle cx="4" cy="8" r="2.4"/><circle cx="9" cy="4.5" r="2.4"/><circle cx="15" cy="5" r="2.4"/><circle cx="19" cy="9.5" r="2.2"/></svg>onsite care</li>
    <li><svg class="paw" viewBox="0 0 22 22"><ellipse cx="11" cy="14.5" rx="6" ry="5.5"/><circle cx="4" cy="8" r="2.4"/><circle cx="9" cy="4.5" r="2.4"/><circle cx="15" cy="5" r="2.4"/><circle cx="19" cy="9.5" r="2.2"/></svg>training</li>
    <li><svg class="paw" viewBox="0 0 22 22"><ellipse cx="11" cy="14.5" rx="6" ry="5.5"/><circle cx="4" cy="8" r="2.4"/><circle cx="9" cy="4.5" r="2.4"/><circle cx="15" cy="5" r="2.4"/><circle cx="19" cy="9.5" r="2.2"/></svg>behavioural consultations</li>
  </ul>

  <svg class="swoosh" viewBox="0 0 290 160" aria-hidden="true">
    <defs>
      <linearGradient id="swoosh-fade" x1="0" y1="1" x2="1" y2="0">
        <stop offset="0" stop-color="#d2dabb" stop-opacity="0"/>
        <stop offset="0.5" stop-color="#d2dabb"/>
        <stop offset="1" stop-color="#d2dabb" stop-opacity="0.3"/>
      </linearGradient>
    </defs>
    <path d="M12 150 C -5 80, 55 8, 145 8 C 205 8, 250 40, 280 115 C 240 60, 195 30, 145 30 C 75 32, 25 80, 12 150 Z" fill="url(#swoosh-fade)"/>
  </svg>

  <address class="contact">
    <div class="contact-name">Rua</div>
    <div class="contact-phone">0498307164</div>
    <div class="contact-web">meadowpawsdemo.com.au</div>
  </address>
</div>
</body>
</html>
```